HOME IMPROVEMENT Business Card

I want a very unique business card. nothing typical and boring. Im open to you ideas. Ive seen cards with gold and silver or color foil and spot UV coatings. Im looking for something that looks cool and grabs attention. I like rounded corners but am open to all suggestions. We are a home improvement company and I will have a presentation folder printed and a catalog printed also and want to keep that same theme. I love the colors in our logo but I am open at looking at a 3rd color that would work with my logo. I hope that helps.
Card should include
Address
Phone
Fax
Email
Website
Target Market(s)
Home owners, people looking to remodel their home
Industry/Entity Type
Home Improvement
Contact Information for Business Card
2871 Maple Crest Avenue Unit 400
Des Plaines, Il 60093
Phone
Direct Line
Email
Website
Font styles to use
Other font styles liked:
- IM OPEN MINDED
Requirements
Must have
- High end quality look nothing boring I like rounded corners but am open minded
Nice to have
- WOW. I want something nice and impressive.
Should not have
- ??? Not sure

```html
<!DOCTYPE html>
<html lang="en">
<head>
<meta charset="utf-8">
<title>Keystone Home Renovation Group – Business Card</title>
<link href="https://fonts.googleapis.com/css2?family=Mulish:wght@400;600;800&display=swap" rel="stylesheet">
<style>
  :root {
    --green: #0b9a48;
    --green-text: #12a04c;
    --navy: #0f1347;
    --white: #ffffff;
    --ink: #1c1f4a;
    --page: #ecedef;
  }
  * { box-sizing: border-box; margin: 0; padding: 0; }
  html, body { width: 1200px; height: 900px; overflow: hidden; }
  body {
    background: var(--page);
    font-family: "Mulish", "Avenir", sans-serif;
    position: relative;
  }
  .card {
    position: absolute;
    width: 620px;
    height: 354px;
    border-radius: 26px;
    overflow: hidden;
    box-shadow: 0 10px 28px rgba(0,0,0,.18);
  }

  /* Front */
  .card-front { left: 110px; top: 60px; background: var(--green); }
  .front-rule {
    position: absolute;
    height: 3px;
    background: var(--white);
  }
  .front-rule.left { left: 0; width: 210px; top: 270px; }
  .front-rule.right { right: 0; width: 175px; top: 150px; }
  .front-brand {
    position: absolute;
    left: 220px;
    top: 138px;
    color: var(--navy);
    font-weight: 800;
    line-height: 1;
  }
  .front-brand .brand-name { font-size: 62px; letter-spacing: -1px; }
  .front-brand .brand-sub { font-size: 15px; letter-spacing: 4.4px; margin-top: 10px; }

  /* Back */
  .card-back { left: 470px; top: 480px; background: var(--white); }
  .back-band {
    position: absolute;
    left: 0; top: 0; bottom: 0;
    width: 108px;
    background: var(--navy);
  }
  .back-content {
    position: absolute;
    left: 148px;
    top: 34px;
    color: var(--ink);
  }
  .back-brand { color: var(--navy); font-weight: 800; line-height: 1; }
  .back-brand .brand-name { font-size: 44px; letter-spacing: -1px; }
  .back-brand .brand-sub { font-size: 11px; letter-spacing: 3.2px; margin-top: 7px; }
  .person-name {
    color: var(--green-text);
    font-size: 25px;
    font-weight: 400;
    margin-top: 16px;
    line-height: 1.1;
  }
  .person-title { font-size: 15px; margin-top: 2px; margin-left: 2px; }
  .contact-list { list-style: none; margin-top: 12px; }
  .contact-list li {
    display: flex;
    align-items: center;
    gap: 12px;
    font-size: 16px;
    letter-spacing: .4px;
    line-height: 24px;
  }
  .contact-list svg { width: 14px; height: 14px; fill: var(--green); flex: none; }
  .contact-list b { font-weight: 800; }
  .address { font-size: 16px; line-height: 21px; margin-top: 6px; margin-left: 26px; }
</style>
</head>
<body>

<section class="card card-front" aria-label="Card front">
  <div class="front-rule left"></div>
  <div class="front-rule right"></div>
  <div class="front-brand">
    <div class="brand-name">Keystone</div>
    <div class="brand-sub">HOME RENOVATION GROUP</div>
  </div>
</section>

<section class="card card-back" aria-label="Card back">
  <div class="back-band"></div>
  <div class="back-content">
    <div class="back-brand">
      <div class="brand-name">Keystone</div>
      <div class="brand-sub">HOME RENOVATION GROUP</div>
    </div>
    <div class="person-name">Daniel Harlow</div>
    <div class="person-title">President</div>
    <ul class="contact-list">
      <li>
        <svg viewBox="0 0 16 16" aria-hidden="true"><path d="M3.6 1.2l2.3 2.3-1.3 2c.9 2 2.5 3.6 4.4 4.5l2-1.3 2.3 2.3-1.6 2.2C7 13.4 2.6 9 1.6 3z"/></svg>
        <span>312. 555. 0147</span>
      </li>
      <li>
        <svg viewBox="0 0 16 16" aria-hidden="true"><path d="M4 1h8v4H4zM1 6h14v6h-3v3H4v-3H1zm4 4v3h6v-3z"/></svg>
        <span>312. 555. 0148</span>
      </li>
      <li>
        <svg viewBox="0 0 16 16" aria-hidden="true"><path d="M1 3h14v10H1zm1.5 1.2L8 8.5l5.5-4.3z"/></svg>
        <span>dan@keystonehome.com</span>
      </li>
      <li>
        <svg viewBox="0 0 16 16" aria-hidden="true"><path d="M8 1a7 7 0 110 14A7 7 0 018 1zm0 1.5c-1 1.4-1.6 3.3-1.6 5.5S7 12.1 8 13.5c1-1.4 1.6-3.3 1.6-5.5S9 3.9 8 2.5zM2.6 7.3h10.8v1.4H2.6z"/></svg>
        <span>www.<b>keystonehome</b>.com</span>
      </li>
    </ul>
    <div class="address">2871 Maple Crest Avenue Unit 400<br>Des Plaines, IL 60093</div>
  </div>
</section>

</body>
</html>
```